My company Tilt Foundry, founded in 2004 and based in downtown Brooklyn, NY, is a design firm specializing in furniture and residential projects, primarily apartments in New York City but also houses in the New York area. The built projects are distinctly modern, and the furniture (large wooden constructions that hold books and objects) border on sculpture. I also do a fair amount of photography and drawing, so my ideal client is someone who collects current art and photography and wants a space commensurate with that interest. The purpose of the website is twofold. First, to attract a clientele for residential projects who have a strong interest in contemporary art, and secondly, to develop a platform for selling my furniture on a made-to-order basis. The website, and especially the landing page, should visualize my preference for raw materials-construction lumber, plywood, concrete, exposed bolts and screws, etc. I like bold colors, graffiti, accidental marks, and all species of imperfection. Slick and ultra-stylized is not my thing. With regard to typeface, I like it simple and unadorned, but assertive, and handwritten is an option as long as it is bold. The landing page could simply be a background featuring one of the above preferences, with TILT FOUNDRY overlaid in black (or colored?) type and a small 'enter' button to an index page, but I'm open to suggestions. See additional directions below...Thanks!

Target Market(s)

People interested in contemporary art, photography, architecture and design

Industry/Entity Type

Residential

Requirements
Must have
• All I would like to see initially is a landing page and index page. The landing page as stated above should have a material background-see attached photos (any will do) with the company name and enter button.
The index page should include the following categories with links to be designed later: About, Portfolio, Purchase Furniture, Contact. Use a second material background from the attached photos for the index page. NOTE: please use the concrete slab photo on one of the pages, the other page can have either plywood or carboard, whichever works best for your design. If you want to replicate the ply or cardboard in a grid that's fine too
Should not have
• Since I take an ipad when I meet with clients the site cannot utilize Flash. Also no sound.

```html
<!DOCTYPE html>
<html lang="en">
<head>
<meta charset="UTF-8">
<title>Tilt Foundry</title>
<link rel="stylesheet" href="https://fonts.googleapis.com/css2?family=Oswald:wght@700&family=Crimson+Text:wght@600&family=Kalam:wght@400&display=swap">
<style>
  :root {
    --wood-dark: #1e1511;
    --wood-mid: #2c211b;
    --wood-light: #3a2b22;
    --paper-light: #c9bb91;
    --paper-mid: #b3a479;
    --paper-dark: #8f8259;
    --paper-edge: #e0cf86;
    --name-ink: #ffffff;
    --tagline-ink: #e9e2d0;
    --button-top: #d9ac4f;
    --button-bottom: #9d6e22;
    --button-border: #7a5519;
    --button-ink: #2a1c0c;
  }
  * { margin: 0; padding: 0; box-sizing: border-box; }
  html, body { width: 1200px; height: 640px; overflow: hidden; background: var(--wood-dark); }
  .landing {
    position: relative;
    width: 1200px;
    height: 640px;
    overflow: hidden;
    background: linear-gradient(90deg, var(--wood-dark) 0%, var(--wood-mid) 30%, var(--wood-light) 50%, var(--wood-mid) 72%, var(--wood-dark) 100%);
  }
  .paper {
    position: absolute;
    inset: 0;
    width: 1200px;
    height: 640px;
  }
  .brand {
    position: absolute;
    top: 98px;
    left: 0;
    width: 1200px;
    text-align: center;
  }
  .brand-name {
    font-family: "Oswald", sans-serif;
    font-weight: 700;
    font-size: 136px;
    line-height: 1;
    letter-spacing: 1px;
    color: var(--name-ink);
  }
  .tagline {
    position: absolute;
    top: 262px;
    right: 250px;
    font-family: "Crimson Text", serif;
    font-weight: 600;
    font-size: 21px;
    color: var(--tagline-ink);
  }
  .enter-button {
    position: absolute;
    left: 430px;
    top: 472px;
    width: 322px;
    height: 84px;
    display: flex;
    align-items: center;
    justify-content: center;
    border-radius: 4px;
    border: 1px solid var(--button-border);
    background: linear-gradient(180deg, var(--button-top) 0%, #c08a34 55%, var(--button-bottom) 100%);
    box-shadow: 0 2px 4px rgba(0, 0, 0, 0.35), inset 0 1px 0 rgba(255, 235, 170, 0.5);
    font-family: "Kalam", cursive;
    font-size: 40px;
    color: var(--button-ink);
    text-decoration: none;
  }
</style>
</head>
<body>
  <main class="landing">
    <svg class="paper" viewBox="0 0 1200 640" role="img" aria-label="Aged paper texture with a torn upper edge">
      <defs>
        <linearGradient id="paperFill" x1="0" y1="0" x2="1" y2="1">
          <stop offset="0" stop-color="#8f8259"/>
          <stop offset="0.35" stop-color="#b3a479"/>
          <stop offset="0.65" stop-color="#c9bb91"/>
          <stop offset="1" stop-color="#b3a479"/>
        </linearGradient>
      </defs>
      <polygon class="paper-back" fill="#e0cf86"
        points="1160,330 1178,318 1200,312 1200,640 1170,640"/>
      <polygon class="paper-front" fill="url(#paperFill)"
        points="0,436 40,432 70,424 96,430 130,418 170,421 210,412 240,416 280,405 320,408 360,398 400,402 440,392 480,395 520,385 560,388 600,376 640,380 680,370 720,373 760,362 800,366 840,356 880,358 920,350 960,352 1000,344 1030,346 1048,324 1056,340 1080,338 1110,334 1140,336 1170,330 1176,640 0,640"/>
    </svg>

    <header class="brand">
      <h1 class="brand-name">TILT FOUNDRY</h1>
    </header>
    <p class="tagline">The Best Furniture Design Solutions</p>

    <a class="enter-button" href="#index">Enter</a>
  </main>
</body>
</html>
```